Trash/recycling can & dumpster cleaning service

We power wash the inside and outside of trash/recycling cans & dumpsters. The water is collected and disposed of properly. We use environmentally safe products that leave your bins looking and smelling new.

Target Market(s)

Homeowners/renters, HOA's, Restaurant/Bars, Grocery stores, Hotel & Motels, Vacation homes, and neighborhoods with special rules to be allowed to live there.

Industry/Entity Type

Cleaning Service

Contact Information for Business Card

Bristle Bright Bins, Doug Pemberton-president-(555)555-0173, Marcus Telford-Vice President/treasurer-(555)555-0148, Fairhaven, ND

Font styles to use
Serif

Requirements
Nice to have
• A picture of trash can (real or animated). The colors we would like to use is the same as the picture of Varo shoes in my images, sketches, or document section. Main color the aqua blue w/the bright fluorescent yellow and orange as accent colors.

```html
<!DOCTYPE html>
<html lang="en">
<head>
<meta charset="utf-8">
<title>Bristle Bright Bins – Stationery</title>
<link rel="stylesheet" href="https://fonts.googleapis.com/css2?family=Cinzel:wght@400;700;900&display=swap">
<style>
  :root {
    --stage: #000000;
    --paper: #ffffff;
    --card: #f4f6f7;
    --orange: #f9a11b;
    --aqua: #3ba7dc;
    --ink: #1a1a1a;
    --can-light: #e9ecee;
    --can-mid: #c9ced2;
    --can-dark: #8f959a;
  }
  * { margin: 0; padding: 0; box-sizing: border-box; }
  html, body { width: 1200px; height: 858px; overflow: hidden; background: var(--stage); }
  body { position: relative; font-family: "Cinzel", Georgia, serif; color: var(--ink); }

  .letterhead {
    position: absolute; left: 41px; top: 26px; width: 595px; height: 803px;
    background: var(--paper);
  }
  .letterhead__brand {
    position: absolute; top: 16px; left: 0; width: 100%; text-align: center;
    font-weight: 900; font-size: 33px; color: var(--orange); letter-spacing: 0.2px;
  }
  .letterhead__phone {
    position: absolute; top: 64px; left: 0; width: 100%; text-align: center;
    font-size: 13px;
  }
  .label { color: var(--orange); font-weight: 700; }
  .letterhead__bands { position: absolute; left: 0; bottom: 0; }

  .card {
    position: absolute; left: 696px; width: 452px; height: 258px;
    background: var(--card); overflow: hidden;
  }
  .card--front-a { top: 26px; }
  .card--back { top: 298px; }
  .card--front-b { top: 571px; }

  .can-art { position: absolute; border-radius: 10px 10px 14px 14px; }
  .can-art--main {
    left: 280px; top: 2px; width: 172px; height: 240px;
    background: linear-gradient(90deg, var(--can-dark), var(--can-light) 35%, var(--can-mid) 70%, var(--can-dark));
  }
  .can-art--ghost {
    left: 180px; top: 18px; width: 80px; height: 222px;
    background: linear-gradient(90deg, var(--can-light), #fbfcfc 50%, var(--can-light));
    opacity: 0.8;
  }
  .can-art--pair-left, .can-art--pair-right {
    top: 2px; width: 162px; height: 254px;
    background: linear-gradient(90deg, var(--can-light), #fbfcfc 50%, var(--can-light));
  }
  .can-art--pair-left { left: 56px; }
  .can-art--pair-right { left: 240px; }

  .card__brand {
    position: absolute; left: 18px; top: 33px;
    font-weight: 900; font-size: 25px; color: var(--orange); white-space: nowrap;
  }
  .card--back .card__brand { left: 0; width: 100%; text-align: center; top: 110px; font-size: 26px; }
  .card__name { position: absolute; left: 19px; top: 102px; font-weight: 700; font-size: 14px; color: var(--orange); }
  .card__title { position: absolute; left: 19px; top: 120px; font-size: 11px; }
  .card__city { position: absolute; left: 19px; top: 149px; font-size: 11px; }
  .card__phone { position: absolute; left: 19px; top: 180px; font-size: 11px; }
  .card__bands { position: absolute; left: 0; bottom: 0; }
</style>
</head>
<body>

<section class="letterhead">
  <div class="letterhead__brand">Bristle Bright Bins</div>
  <div class="letterhead__phone"><span class="label">Phone :</span> (555)555-0173</div>
  <svg class="letterhead__bands" width="595" height="32" viewBox="0 0 595 32">
    <polygon points="0,14 391,14 382,32 0,32" fill="var(--aqua)"/>
    <polygon points="414,0 595,0 595,32 386,32" fill="var(--orange)"/>
  </svg>
</section>

<section class="card card--front-a">
  <div class="can-art can-art--ghost" role="img" aria-label="Faint background trash can"></div>
  <div class="can-art can-art--main" role="img" aria-label="Metal trash can with lid"></div>
  <div class="card__brand">Bristle Bright Bins</div>
  <div class="card__name">Doug Pemberton</div>
  <div class="card__title">President</div>
  <div class="card__city">Fairhaven, ND</div>
  <div class="card__phone"><span class="label">Phone :</span> (555)555-0173</div>
  <svg class="card__bands" width="452" height="27" viewBox="0 0 452 27">
    <polygon points="0,11 300,11 293,27 0,27" fill="var(--aqua)"/>
    <polygon points="313,0 452,0 452,27 296,27" fill="var(--orange)"/>
  </svg>
</section>

<section class="card card--back">
  <div class="can-art can-art--pair-left" role="img" aria-label="Faint white trash can with lid"></div>
  <div class="can-art can-art--pair-right" role="img" aria-label="Faint white trash can with open lid"></div>
  <div class="card__brand">Bristle Bright Bins</div>
</section>

<section class="card card--front-b">
  <div class="can-art can-art--ghost" role="img" aria-label="Faint background trash can"></div>
  <div class="can-art can-art--main" role="img" aria-label="Metal trash can with lid"></div>
  <div class="card__brand">Bristle Bright Bins</div>
  <div class="card__name">Marcus Telford</div>
  <div class="card__title">Vice President/treasurer</div>
  <div class="card__city">Fairhaven, ND</div>
  <div class="card__phone"><span class="label">Phone :</span> (555)555-0148</div>
  <svg class="card__bands" width="452" height="27" viewBox="0 0 452 27">
    <polygon points="0,11 300,11 293,27 0,27" fill="var(--aqua)"/>
    <polygon points="313,0 452,0 452,27 296,27" fill="var(--orange)"/>
  </svg>
</section>

</body>
</html>
```